Apricot Variety Sheet - Meadowlark Orchard Co

We are needing a variety sheet that we can hand out that will describe the different apricot vatieties we have available. The attached document has the name of the variety along with a description that will need to be on the sheet. We are looking for a modern, appealing way to display this information on 1 page (if needed, it can be front and back)
Updates

Apologies for the delay; we are overwhelmed with the great design options and will be sorting through them all (across our contests) to pick a collective. Thank you for your patience.

Target Market(s)

Growers and consumers

Industry/Entity Type

Agriculture

Requirements
Must have
• Easy to read
• Natural color palettes to emphasize the agricultural nature
• Clearly show washington as the origin in the title or at the top
Nice to have
• incorporate Apricots in the design

```html
<!DOCTYPE html>
<html lang="en">
<head>
<meta charset="utf-8">
<title>Washington State Apricot Variety Sheet – Meadowlark Orchard Co</title>
<link href="https://fonts.googleapis.com/css2?family=Source+Sans+3:wght@400;600;700;800;900&display=swap" rel="stylesheet">
<style>
  :root {
    --amber: #d99a3a;
    --amber-light: #e9b45a;
    --amber-deep: #b87a26;
    --brown: #3b2416;
    --rule: #4a3324;
    --panel: rgba(34, 112, 44, 0.86);
    --hill-sky: #c9c7c4;
    --hill-tan: #8e7a57;
    --hill-green: #3e5a32;
    --river: #5f7590;
    --title-ink: #3b2212;
    --brand-green: #2e9a3c;
    --variety-orange: #f58220;
    --body-ink: #ffffff;
    --fruit-top: #f7b15a;
    --fruit-bottom: #e07a2a;
  }
  * { margin: 0; padding: 0; box-sizing: border-box; }
  html, body { width: 1200px; height: 927px; overflow: hidden; background: #ffffff; }
  body { font-family: "Source Sans 3", "Myriad Pro", Arial, sans-serif; }

  .sheet { position: relative; width: 1200px; height: 927px; overflow: hidden; }

  .masthead {
    position: absolute; left: 0; top: 0; width: 1200px; height: 156px;
    background: radial-gradient(ellipse at 60% 40%, var(--amber-light), var(--amber) 55%, var(--amber-deep));
  }
  .title {
    position: absolute; left: 78px; top: 30px;
    font-weight: 800; font-size: 41px; line-height: 46px; letter-spacing: 0.5px;
    color: var(--title-ink); text-transform: uppercase;
  }
  .brand {
    position: absolute; left: 694px; top: 44px; display: flex; align-items: center; gap: 14px;
  }
  .brand-dot {
    width: 112px; height: 112px; border-radius: 50%; background: var(--brand-green); flex: none;
    margin-top: 10px;
  }
  .brand-name {
    font-weight: 700; font-size: 29px; line-height: 31px; color: var(--brand-green);
  }

  .top-rule, .bottom-rule { position: absolute; left: 0; width: 1200px; background: var(--rule); }
  .top-rule { top: 156px; height: 7px; }
  .bottom-rule { top: 818px; height: 8px; }

  .landscape {
    position: absolute; left: 0; top: 163px; width: 1200px; height: 655px;
    background: linear-gradient(180deg, var(--hill-sky) 0%, var(--hill-tan) 10%, var(--hill-tan) 22%, var(--river) 30%, var(--hill-green) 45%, #2f4a28 100%);
  }

  .panel {
    position: absolute; top: 169px; height: 649px; background: var(--panel);
    padding: 14px 26px 0 26px; color: var(--body-ink);
  }
  .panel-left { left: 118px; width: 427px; }
  .panel-right { left: 657px; width: 427px; }

  .variety { font-size: 16.5px; line-height: 21.6px; margin-bottom: 5px; }
  .variety-name {
    color: var(--variety-orange); font-weight: 700; font-variant: small-caps; font-size: 19px;
  }

  .fruit {
    position: absolute; border-radius: 50%;
    background: radial-gradient(circle at 40% 35%, var(--fruit-top), var(--fruit-bottom));
  }
  .fruit-left { left: 14px; top: 700px; width: 122px; height: 120px;
    background: radial-gradient(circle at 40% 35%, #f04a3a, #c42a2a 60%, #8ea83a); }
  .fruit-center { left: 515px; top: 694px; width: 130px; height: 128px; }
  .fruit-right { left: 1050px; top: 700px; width: 126px; height: 126px;
    background: radial-gradient(circle at 35% 35%, #f06a3a, #f0983a 70%); }

  .harvest {
    position: absolute; left: 0; top: 826px; width: 1200px; height: 101px;
    background: radial-gradient(ellipse at 50% 60%, #f5b255, #e8872a 70%, #d66f20);
  }
  .site {
    position: absolute; left: 0; top: 866px; width: 1200px; text-align: center;
    font-weight: 700; font-size: 25px; color: var(--title-ink); letter-spacing: 0.3px;
  }
</style>
</head>
<body>
<main class="sheet">
  <header class="masthead" role="img" aria-label="Sunlit orchard trees in warm amber tones">
  </header>
  <h1 class="title">Washington State<br>Apricot Variety Sheet</h1>
  <div class="brand">
    <span class="brand-dot"></span>
    <span class="brand-name">Meadowlark<br>Orchard Co</span>
  </div>
  <div class="top-rule"></div>

  <div class="landscape" role="img" aria-label="Aerial view of orchards along a river valley with rolling hills"></div>

  <section class="panel panel-left">
    <p class="variety"><span class="variety-name">Casselbrite –</span> This medium sized apricot is golden orange with a slight red blush. It has a mild sweet-tart flavor that is good for eating out of hand. Available late June- early July.</p>
    <p class="variety"><span class="variety-name">Goldbar –</span> Moderately juicy, this large oval-shaped apricot has a light yellow-orange with a reddish blush. The flesh is firm, meaty, and has a light orange color. Available late June – end of July.</p>
    <p class="variety"><span class="variety-name">–</span> This special variety has a unique, sweet flavor with a juicy flesh. It is bright orange in color with a bright orange flesh. Available through July.</p>
    <p class="variety"><span class="variety-name">Tasty Rich –</span> This early variety is light yellow-orange colored with a firm texture. Very juicy with an enticing flavor. Available through June.</p>
    <p class="variety"><span class="variety-name">Goldstrike –</span> A larger apricot with light orange, blushed skin. Firm texture with a slight tart taste until fully ripened, then very sweet. Available mid June - mid July.</p>
    <p class="variety"><span class="variety-name">Riland –</span> Very aromatic and sweet, this apricot is orange with a red blush. It has a yellow-orange colored flesh and a round shape. Available mid-June to end of July.</p>
  </section>

  <section class="panel panel-right">
    <p class="variety"><span class="variety-name">Rival –</span> Great flavor with a fine, firm texture distinguishes this large oval-shaped apricot. The skin is light orange with a red blush. The flesh is a lush deep orange color. Available early July- early August.</p>
    <p class="variety"><span class="variety-name">Robada –</span> This jumbo apricot has a delicious floral flavor with a firm texture. Bright orange, with a deep red blush over nearly half its surface. Available early June.</p>
    <p class="variety"><span class="variety-name">Perfection –</span> This classic large oval apricot is deep orange with an oblong shape and firm texture. The flesh is a yellow/orange color that is very sweet and full of flavor. Available mid July - mid August.</p>
    <p class="variety"><span class="variety-name">Patterson –</span> This apricot has a well-balanced flavor and an excellent shelf life. This is perfect for canning or drying. It has streaked red over yellow skin, with a firm flesh. Available mid – late June.</p>
    <p class="variety"><span class="variety-name">Tomcot –</span> Tangy, sweet flavor with a firm texture. This oval apricot is light orange with a slight blush color. The flesh is a dark orange. Available late June – late July.</p>
    <p class="variety"><span class="variety-name">Goldrich –</span> This apricot is round with a bright orange skin color and a deep orange flesh. It has a mild, sweet flavor with a firm texture. Available early July – mid August.</p>
  </section>

  <div class="fruit fruit-left" role="img" aria-label="Red and green blushed stone fruit"></div>
  <div class="fruit fruit-center" role="img" aria-label="Ripe golden apricot"></div>
  <div class="fruit fruit-right" role="img" aria-label="Blushed apricot with a leaf"></div>

  <div class="bottom-rule"></div>
  <footer class="harvest" role="img" aria-label="Pile of ripe apricots"></footer>
  <p class="site">www.meadowlarkorchard.com</p>
</main>
</body>
</html>
```